Groovy little Insurance brokerage needs a new look

We have a new logo, but need to work out how to make it work for us!
We are a small insurance broking firm (three staff with different focus and styles), with lots of energy, experience and enthusiasm. A focus on both commercial and domestic market. We would like our cards to show a fresh look - while veering away from the 'run of the mill' insurance industry (often dull) approach.
Updates

Thanks to all for your concepts.

Had some great ideas come back, now just the process of picking which one is going to work best for us...
Will advise when we've had an opportunity to review.

Thanks!
From the team at
Kestrel Dunmore Insurance Brokers

Thanks SO much to all of your for your great designs.  Now just a process of sorting out the favorites.  If yours is eliminated, just want to say a collective thank you for your efforts!

Industry/Entity Type

Business

```html
<!DOCTYPE html>
<html lang="en">
<head>
<meta charset="utf-8">
<title>Kestrel Dunmore Insurance Brokers – Business Card</title>
<link href="https://fonts.googleapis.com/css2?family=Lato:wght@400;700;900&display=swap" rel="stylesheet">
<style>
  :root {
    --backdrop: #2b2b2b;
    --card: #ffffff;
    --teal: #10a9c6;
    --teal-light: #a9dbe6;
    --ink: #1b1718;
  }
  html, body {
    margin: 0;
    width: 1200px;
    height: 1000px;
    overflow: hidden;
    background: var(--backdrop);
    font-family: "Lato", sans-serif;
  }
  .card {
    position: absolute;
    left: 180px;
    top: 250px;
    width: 840px;
    height: 500px;
    background: var(--card);
    box-sizing: border-box;
    display: flex;
    flex-direction: column;
    align-items: center;
  }
  .brand {
    margin-top: 92px;
    display: flex;
    align-items: center;
    gap: 22px;
  }
  .brand-square {
    width: 110px;
    height: 110px;
    display: block;
    flex: none;
  }
  .brand-name {
    font-weight: 900;
    font-size: 34px;
    line-height: 1.1;
    letter-spacing: 1px;
    color: var(--ink);
    text-transform: uppercase;
    max-width: 420px;
  }
  .holder-name {
    margin: 48px 0 24px;
    font-weight: 700;
    font-size: 26px;
    letter-spacing: 1.5px;
    color: var(--teal);
    text-transform: uppercase;
  }
  .contact {
    margin: 0;
    padding: 0;
    list-style: none;
    text-align: center;
    font-size: 19px;
    line-height: 1.45;
  }
  .contact-label {
    font-weight: 700;
    color: var(--teal);
    margin-right: 6px;
  }
  .contact-value {
    font-weight: 700;
    color: var(--ink);
    letter-spacing: 0.5px;
  }
  .web-tab {
    position: absolute;
    bottom: 0;
    left: 50%;
    transform: translateX(-50%);
    width: 300px;
    height: 44px;
    background: var(--teal);
    border-radius: 6px 6px 0 0;
    color: #ffffff;
    font-weight: 700;
    font-size: 19px;
    letter-spacing: 1.5px;
    display: flex;
    align-items: center;
    justify-content: center;
  }
  .card-edge {
    position: absolute;
    left: 0;
    right: 0;
    bottom: -8px;
    height: 8px;
    background: var(--teal-light);
  }
</style>
</head>
<body>
  <article class="card">
    <header class="brand">
      <svg class="brand-square" viewBox="0 0 110 110" aria-hidden="true">
        <rect width="110" height="110" fill="var(--teal-light)"/>
      </svg>
      <div class="brand-name">Kestrel Dunmore Insurance Brokers</div>
    </header>

    <h1 class="holder-name">Kestrel Dunmore</h1>

    <ul class="contact">
      <li><span class="contact-label">Phone:</span><span class="contact-value">021 555 0184</span></li>
      <li><span class="contact-label">Email:</span><span class="contact-value">kestrel@kdib.co.nz</span></li>
      <li><span class="contact-label">Address:</span><span class="contact-value">P.O. Box 48 Dunmore Bay, NZ 7010</span></li>
    </ul>

    <div class="web-tab">www.kdib.co.nz</div>
    <div class="card-edge"></div>
  </article>
</body>
</html>
```